Brightvantage.com tech company website

Current site is www.brightvantage.com. The site will tell you about our company.

Designs we like are:
http://megainfo.quellorix.com
www.trelvo.com
www.morvasket.com

Target Market(s)

B2B

Industry/Entity Type

It Company

Coding

Coded - Design and coding required

Number of Pages Required

5+ page

Requirements
Must have
• We want to entice without giving away too much info. We like graphics and colors. But website must look official and credible.

```html
<!DOCTYPE html>
<html lang="en">
<head>
<meta charset="utf-8">
<title>Brightvantage.com — Big Data & Analytics</title>
<link rel="stylesheet" href="https://fonts.googleapis.com/css2?family=Special+Elite&family=Oswald:wght@400;500;600&family=Raleway:wght@300;400;700&family=Open+Sans:wght@400;600;700&display=swap">
<style>
:root{
  --navy:#0b1530;
  --navy-deep:#060d20;
  --blue:#1a3cf0;
  --blue-light:#cfd8f5;
  --ink:#1b1b1b;
  --text:#7a7a7a;
  --muted:#a9a9a9;
  --gray-band:#ededed;
  --gray-dark:#5a5d63;
  --white:#ffffff;
}
*{box-sizing:border-box;margin:0;padding:0}
html,body{width:1200px;height:4500px;overflow:hidden;background:var(--white)}
body{position:relative;font-family:"Open Sans",sans-serif;color:var(--ink)}
section,header,footer{position:absolute;left:0;width:1200px}
.abs{position:absolute}
p{font-size:13px;line-height:1.6;color:var(--text)}

/* hero */
.hero{top:0;height:600px;background:linear-gradient(180deg,#0d1a3a 0%,#0a1734 45%,#050b1c 100%)}
.hero-photo{position:absolute;inset:0;background:radial-gradient(ellipse at 50% 40%,rgba(60,100,170,.45),transparent 65%),linear-gradient(90deg,rgba(20,40,90,.5),rgba(5,10,25,.2),rgba(20,40,90,.5))}
.brand{left:20px;top:14px;display:flex;align-items:center;gap:8px;font-family:"Oswald",sans-serif;font-weight:600;font-size:22px;letter-spacing:1px;color:var(--white)}
.brand-mark{width:18px;height:18px;background:var(--blue)}
.nav{right:20px;top:18px;display:flex;gap:10px;font-family:"Special Elite",monospace;font-size:15px;color:var(--white);white-space:nowrap}
.hero-title{top:228px;width:100%;text-align:center;font-family:"Special Elite",monospace;font-size:36px;letter-spacing:3px;color:var(--white);white-space:nowrap}
.hero-sub{top:282px;left:260px;width:680px;text-align:center;font-family:"Special Elite",monospace;font-size:25px;line-height:1.3;color:var(--white)}
.hero-btn{top:396px;left:410px;width:380px;height:46px;background:var(--blue);color:var(--white);font-family:"Oswald",sans-serif;font-size:17px;letter-spacing:1px;display:flex;align-items:center;justify-content:center}

/* what is big data */
.what{top:600px;height:920px}
.section-title{width:100%;text-align:center;font-family:"Raleway",sans-serif;font-weight:300;font-size:64px;letter-spacing:2px;color:var(--ink)}
.section-title b{color:var(--blue);font-weight:700}
.what .section-title{top:40px}
.chart{left:240px;top:155px;width:720px;height:130px}
.intro{top:300px;left:210px;width:780px;text-align:center;font-size:11px;color:var(--muted)}
.col-title{font-family:"Oswald",sans-serif;font-weight:600;font-size:22px;line-height:1.2;color:var(--ink)}
.left-col{left:170px;top:425px;width:470px}
.left-col .col-title{font-size:18px;white-space:nowrap}
.left-col p{margin-top:10px}
.read-more{display:block;margin-top:10px;font-size:12px;color:var(--blue);text-transform:uppercase}
.left-illus{left:170px;top:575px;width:450px;height:200px;background:linear-gradient(135deg,#3a2fe0,#5a4df0);}
.right-col{left:800px;top:420px;width:230px}
.right-col p{margin-top:10px;font-size:12px}
.quiz{margin-top:12px;font-family:"Oswald",sans-serif;font-weight:600;font-size:30px;line-height:1.05;color:var(--ink)}
.quiz small{display:block;font-size:22px}

/* survey */
.survey{top:1520px;height:520px;background:var(--gray-band)}
.video{left:60px;top:40px;width:540px;height:420px;background:var(--white);box-shadow:0 2px 6px rgba(0,0,0,.12)}
.video-illus{position:absolute;left:0;top:0;width:540px;height:380px;background:radial-gradient(circle at 50% 40%,#dfe8f5,#ffffff 60%)}
.video-bar{position:absolute;left:0;bottom:0;width:540px;height:40px;background:#222}
.survey-card{left:610px;top:0;width:590px;height:520px;background:var(--white)}
.survey-card h2{position:absolute;left:40px;top:40px;width:500px;font-family:"Oswald",sans-serif;font-weight:500;font-size:30px;letter-spacing:3px;line-height:1.3;color:var(--ink)}
.survey-card p{position:absolute;left:40px;width:500px;font-size:12px;color:var(--muted)}
.dots{display:flex;gap:6px}
.dot{width:9px;height:9px;border-radius:50%;border:1px solid #999}
.dot.on{background:#999}

/* articles band */
.articles-band{top:2040px;height:190px;background:linear-gradient(180deg,#6b6f76,#4e5258)}
.articles-band h2{position:absolute;top:72px;width:100%;text-align:center;font-family:"Oswald",sans-serif;font-weight:500;font-size:42px;letter-spacing:8px;color:var(--white)}
.circle-btn{width:32px;height:32px;border-radius:50%;background:var(--blue);display:flex;align-items:center;justify-content:center}

.articles{top:2230px;height:430px}
.card{top:110px;width:270px}
.card-img{width:270px;height:160px}
.card h3{margin-top:26px;text-align:center;font-size:12px;font-weight:700;color:#2a3a8a}
.card p{margin-top:14px;text-align:center;font-size:11px;color:var(--muted)}

/* invite */
.invite{top:2660px;height:240px;background:var(--blue)}
.invite span{position:absolute;top:110px;width:100%;text-align:center;font-family:"Oswald",sans-serif;font-size:16px;letter-spacing:2px;color:var(--white)}

/* testimonial */
.testimonial{top:2900px;height:660px;background:linear-gradient(180deg,#3a3f4a,#2c3039 50%,#40454f)}
.testimonial .photo{position:absolute;inset:0;background:radial-gradient(ellipse at 50% 45%,rgba(120,130,150,.35),transparent 70%)}
.quote-icon{left:580px;top:150px;width:44px;height:44px;border-radius:50%;background:var(--white)}
.quote{top:236px;left:330px;width:540px;text-align:center;font-size:15px;font-weight:600;line-height:1.5;color:var(--white)}
.quote-name{top:300px;width:100%;text-align:center;font-size:12px;color:#ddd}
.arrow-circle{width:30px;height:30px;border-radius:50%;background:#8a8d93;display:flex;align-items:center;justify-content:center}

/* subscribe */
.subscribe{top:3560px;height:330px;background:linear-gradient(180deg,#44474d,#33363b);z-index:2}
.subscribe h2{position:absolute;top:115px;width:100%;text-align:center;font-family:"Oswald",sans-serif;font-weight:400;font-size:15px;letter-spacing:2px;color:var(--white)}
.sub-input{left:420px;top:156px;width:280px;height:46px;background:var(--white)}
.sub-btn{left:700px;top:156px;width:80px;height:46px;background:var(--blue);color:var(--white);font-family:"Oswald",sans-serif;font-size:15px;display:flex;align-items:center;justify-content:center}

/* contact */
.contact{top:3890px;height:520px;background:#f2f2f2}
.contact h2{position:absolute;top:90px;width:100%;text-align:center;font-family:"Oswald",sans-serif;font-weight:400;font-size:18px;letter-spacing:3px;color:var(--ink)}
.info-box{top:220px;width:250px;height:170px;background:var(--white);text-align:center}
.info-box strong{display:block;margin-top:36px;font-family:"Oswald",sans-serif;font-size:30px;font-weight:400;color:var(--blue)}
.info-box span{display:block;margin-top:10px;font-size:12px;color:var(--text)}
.social{top:475px;left:535px;display:flex;gap:20px}
.social i{display:block;width:28px;height:28px;border-radius:50%;background:#2d2f33}

/* footer */
.footer{top:4410px;height:90px;background:var(--blue);color:var(--white);font-size:12px}
.footer .copy{left:60px;top:38px}
.footer .phone{right:60px;top:38px}
</style>
</head>
<body>

<header class="hero">
  <div class="hero-photo" role="img" aria-label="Dark blue backdrop of streaming binary code"></div>
  <div class="brand abs"><span class="brand-mark"></span>BRIGHTVANTAGE</div>
  <nav class="nav abs"><span>HOME</span><span>ABOUT</span><span>BIG DATA AND ANALYTICS</span><span>PERCEPTION AND INFLUENCE</span><span>CASE STUDIES</span><span>CONTACT</span></nav>
  <h1 class="hero-title abs">BETTING ON BIG DATA &amp; ANALYTICS TO WIN</h1>
  <p class="hero-sub abs">Increase your odds by tackling cultural, strategic and operational hurdles.</p>
  <div class="hero-btn abs">GET CORVANE RESEARCH &amp; KEY FINDINGS</div>
</header>

<section class="what">
  <h2 class="section-title abs">WHAT IS <b>BIG DATA</b>?</h2>
  <svg class="chart abs" viewBox="0 0 720 130" aria-label="Bar chart of data growth">
    <g fill="#c9d3f2">
      <rect x="0" y="118" width="720" height="2"/>
      <rect x="160" y="70" width="30" height="48"/><rect x="200" y="50" width="30" height="68"/>
      <rect x="240" y="80" width="30" height="38"/><rect x="280" y="30" width="30" height="88"/>
      <rect x="320" y="60" width="30" height="58"/><rect x="360" y="20" width="30" height="98"/>
      <rect x="400" y="45" width="30" height="73"/><rect x="440" y="10" width="30" height="108"/>
      <rect x="480" y="55" width="30" height="63"/><rect x="520" y="35" width="30" height="83"/>
    </g>
  </svg>
  <p class="intro abs">Big data describes the huge volume of structured and unstructured information that floods a business every day. What matters is not the amount of data but what companies do with it. Data can be analysed for insights that lead to better decisions and smarter strategic business moves across every team.</p>

  <div class="left-col abs">
    <h3 class="col-title">BIG DATA - IT'S HERE. IT'S NOW. IT'S TRANSFORMATIVE.</h3>
    <p>Every day, businesses generate more data than ever before. Those who turn it into clear insight move faster, serve customers better and find new sources of growth.</p>
    <span class="read-more">Read more</span>
  </div>
  <div class="left-illus abs" role="img" aria-label="Illustration of hands holding devices above streams of data"></div>

  <div class="right-col abs">
    <h3 class="col-title" style="font-size:16px">SMARTER ANSWERS TO BIG DATA QUESTIONS</h3>
    <p>Find out how leading teams put analytics to work, where they start and which early wins build lasting momentum across the whole company.</p>
    <div class="quiz"><small>Take the</small>BIG DATA QUIZ</div>
    <p>Test what you know in five minutes and see how your plans compare with peers in your field today.</p>
  </div>
</section>

<section class="survey">
  <div class="video abs">
    <div class="video-illus" role="img" aria-label="Video still showing a round data network icon"></div>
    <div class="video-bar"></div>
  </div>
  <div class="survey-card abs">
    <h2>CORVANE INSIGHTS SURVEY ON BIG DATA &amp; ANALYTICS</h2>
    <p style="top:150px">A global survey of senior executives reveals how companies use data to compete, and which hurdles still slow them down on the road to results.</p>
    <p style="top:225px">Most leaders say analytics already shapes key decisions, yet few feel their teams have the skills and tools to act on it fully.</p>
    <p style="top:285px">Read the findings to learn what sets the leaders apart and how to close the gap.</p>
    <div class="dots abs" style="left:285px;top:465px"><span class="dot on"></span><span class="dot"></span></div>
  </div>
</section>

<section class="articles-band">
  <h2>LATEST ARTICLES</h2>
  <div class="circle-btn abs" style="left:584px;top:142px">
    <svg width="12" height="8" viewBox="0 0 12 8"><path d="M1 1l5 5 5-5" stroke="#fff" stroke-width="2" fill="none"/></svg>
  </div>
</section>

<section class="articles">
  <div class="card abs" style="left:170px">
    <div class="card-img" role="img" aria-label="Article image in purple and blue tones" style="background:linear-gradient(135deg,#5a2a9a,#2f5fd0)"></div>
    <h3>Back to the Future: What is Big Data?</h3>
    <p>A look at how the idea of big data has grown and what it means for business leaders now.</p>
  </div>
  <div class="card abs" style="left:460px">
    <div class="card-img" role="img" aria-label="Article image of dark teal data graphics" style="background:linear-gradient(135deg,#16383e,#2a6b6b)"></div>
    <h3>Five Years Later: What Is Big Data?</h3>
    <p>Five years on, we revisit the definition and see which predictions proved right in practice.</p>
  </div>
  <div class="card abs" style="left:740px">
    <div class="card-img" role="img" aria-label="Article image of large data lettering in blue" style="background:linear-gradient(135deg,#ffffff,#dbe4f7)"></div>
    <h3 style="color:#555;letter-spacing:1px">PIXEL PERFECTION</h3>
    <p>Why clean, well-shaped data is the base for every chart, model and decision you make.</p>
  </div>
  <div class="dots abs" style="left:580px;top:410px"><span class="dot on"></span><span class="dot"></span></div>
</section>

<section class="invite"><span>INVITE YOUR FRIENDS</span></section>

<section class="testimonial">
  <div class="photo" role="img" aria-label="Overhead photo of a desk with computer, tablet and notebook"></div>
  <div class="quote-icon abs"></div>
  <p class="quote abs">These guys are just incredible! I was able to get my project done in just 7 days. I mean AMAZING service! Highly recommended.</p>
  <p class="quote-name abs">Jordan Ellery</p>
  <div class="abs" style="left:568px;top:378px;display:flex;gap:4px">
    <div class="arrow-circle"><svg width="8" height="12" viewBox="0 0 8 12"><path d="M6 1L1 6l5 5" stroke="#fff" stroke-width="2" fill="none"/></svg></div>
    <div class="arrow-circle"><svg width="8" height="12" viewBox="0 0 8 12"><path d="M2 1l5 5-5 5" stroke="#fff" stroke-width="2" fill="none"/></svg></div>
  </div>
</section>

<section class="subscribe" role="img" aria-label="Dark photo of hands typing on a keyboard">
  <h2>SUBSCRIBE TO STAY IN THE LOOP</h2>
  <div class="sub-input abs"></div>
  <div class="sub-btn abs">SEND</div>
  <div class="circle-btn abs" style="left:584px;top:314px">
    <svg width="12" height="8" viewBox="0 0 12 8"><path d="M1 1l5 5 5-5" stroke="#fff" stroke-width="2" fill="none"/></svg>
  </div>
</section>

<section class="contact">
  <h2>DROP US A LINE</h2>
  <svg class="abs" style="left:594px;top:128px" width="12" height="8" viewBox="0 0 12 8"><path d="M1 1l5 5 5-5" stroke="#333" stroke-width="2" fill="none"/></svg>
  <div class="info-box abs" style="left:170px"><strong>9</strong><span>Level 9, 48 Harlow St, Kestrel</span></div>
  <div class="info-box abs" style="left:470px"><strong>2</strong><span>Phone<br>+61 2 5550 1844</span></div>
  <div class="info-box abs" style="left:770px"><strong>3</strong><span>Email<br>hello@brightvantage.com</span></div>
  <div class="social abs"><i></i><i></i><i></i></div>
</section>

<footer class="footer">
  <span class="copy abs">© Brightvantage.com. All rights reserved.</span>
  <span class="phone abs">+61 2 5550 1844</span>
</footer>

</body>
</html>
```